Not-for-profit Community Law Business Card

Not-for-Profit community law firm are looking for new business card design to accompany a new logo.
The cards are to assist the organisation in reaching their strategic objective of generating greater networking amongst the community; specifically with other service providers, clients, and community influencers.
It should stand out. Be professional, strong, creative, clear in detail. The logo should be a major feature of the design.
Updates

Hi All,

Thank you for the submissions so far. I have uploaded the logo and colour details again, as requested. If you have any further issues downloading them or need a different format please contact me on rosa_pellin@vtq.example.au

Kind regards,

Industry/Entity Type

Law Firm

Requirements
Must have
• Logo (attached)
Person's name
Position
Phone
Fax
Email
PO Box address
Website
Colours from the logo.

```html
<!DOCTYPE html>
<html lang="en">
<head>
<meta charset="utf-8">
<title>Harbour Lane Legal Centre – Business Card</title>
<link rel="stylesheet" href="https://fonts.googleapis.com/css2?family=Open+Sans:wght@400;600;700&display=swap">
<style>
  :root {
    --paper: #f4f5f7;
    --navy: #27378a;
    --blue: #3457b2;
    --brand-blue: #1f5fb8;
    --mist: #c3c8e6;
  }
  html, body {
    margin: 0;
    padding: 0;
    overflow: hidden;
    background: #ffffff;
  }
  .card {
    position: relative;
    width: 1200px;
    height: 686px;
    overflow: hidden;
    background: radial-gradient(circle at 70% 60%, #fbfbfc 0%, var(--paper) 70%);
    font-family: "Open Sans", Arial, sans-serif;
  }
  .brand-dot {
    position: absolute;
    left: 84px;
    top: 78px;
    width: 140px;
    height: 140px;
    border-radius: 50%;
    background: var(--brand-blue);
  }
  .brand-name {
    position: absolute;
    left: 252px;
    top: 128px;
    margin: 0;
    color: var(--brand-blue);
    font-weight: 600;
    line-height: 1.1;
  }
  .brand-name .line-main {
    display: block;
    font-size: 58px;
    letter-spacing: 2px;
  }
  .brand-name .line-sub {
    display: block;
    font-size: 28px;
    letter-spacing: 4px;
    margin-left: 214px;
    margin-top: 2px;
  }
  .backdrop-circle {
    position: absolute;
    left: 840px;
    top: 300px;
    width: 400px;
    height: 400px;
    border-radius: 50%;
    background: var(--mist);
    opacity: 0.55;
  }
  .person {
    position: absolute;
    left: 79px;
    top: 305px;
  }
  .person-name {
    margin: 0;
    font-size: 40px;
    font-weight: 700;
    color: var(--navy);
    line-height: 1.2;
  }
  .person-role {
    margin: 0;
    font-size: 37px;
    font-weight: 400;
    color: var(--blue);
    line-height: 1.3;
  }
  .contact {
    position: absolute;
    left: 79px;
    top: 396px;
    margin: 0;
    font-style: normal;
    font-size: 34px;
    line-height: 46px;
    color: var(--blue);
  }
  .contact span { display: block; }
</style>
</head>
<body>
  <main class="card">
    <div class="backdrop-circle" aria-hidden="true"></div>

    <div class="brand-dot" aria-hidden="true"></div>
    <h1 class="brand-name">
      <span class="line-main">HARBOUR LANE</span>
      <span class="line-sub">LEGAL CENTRE INC.</span>
    </h1>

    <section class="person">
      <p class="person-name">Firstname Lastname</p>
      <p class="person-role">Manager</p>
    </section>

    <address class="contact">
      <span>PO Box 118 - Baywater Vale 2399</span>
      <span>Phone: 02 4901 5570 - Fax: 02 4901 5571</span>
      <span>Email: name@harbourlanelegal.org</span>
      <span>Site: www.harbourlanelegal.org</span>
    </address>
  </main>
</body>
</html>
```